K&B RESTORATION

I want a brochure similiar to the example i've attached.
My company name is K&B Restoration. The website is: K-B-Restoration.com.
The phone number is 404.555.0173.

I don't like the "yellow" being the main color of the example so I'm open to suggestions. I want something CLEAN & Simple, like our logo . This will be a bi fold brochure

```html
<!DOCTYPE html>
<html lang="en">
<head>
<meta charset="utf-8">
<title>K&amp;B Restoration – Bi-fold Brochure</title>
<link href="https://fonts.googleapis.com/css2?family=Anton&family=Rubik:wght@400;500;700&display=swap" rel="stylesheet">
<style>
:root{
  --red:#a6223b;
  --red-deep:#8e1a30;
  --ink:#111;
  --white:#fff;
  --stage:#a3a3a3;
  --text:#2a2a2a;
  --body:"Rubik",Arial,sans-serif;
  --display:"Anton",Impact,sans-serif;
}
*{margin:0;padding:0;box-sizing:border-box}
html,body{width:1200px;height:1200px;overflow:hidden;background:var(--stage);font-family:var(--body)}
.canvas{position:relative;width:1200px;height:1200px}
.abs{position:absolute}

/* outer spread */
.outer{left:219px;top:47px;width:763px;height:539px;background:var(--white)}
.back-cover{left:0;top:0;width:462px;height:539px;background:linear-gradient(90deg,#a8233d 0%,#b02a45 60%,#9a1f37 83%,#8f1c33 100%)}
.brand{font-family:var(--body);font-weight:500;letter-spacing:.5px}
.back-brand{left:105px;top:221px;width:126px;height:52px;border:1.5px solid var(--white);display:flex;align-items:center;justify-content:center;color:var(--white);font-size:15px}
.contact-bar{left:0;top:494px;width:462px;height:31px;background:var(--ink);color:var(--white);font-size:12px;font-weight:500;display:flex;align-items:center;gap:14px;padding-left:72px}
.contact-bar span{display:flex;align-items:center;gap:5px}
.front-brand{left:500px;top:24px;width:211px;height:67px;display:flex;align-items:center;justify-content:center}
.front-brand .name{border:1.5px solid var(--ink);padding:14px 18px;font-size:20px;color:var(--ink)}
.frame-top{left:421px;top:119px;width:343px;height:281px;border-left:4px solid var(--ink);border-top:4px solid var(--ink)}
.frame-bottom{left:425px;top:391px;width:306px;height:4px;background:var(--ink)}
.photo{background:linear-gradient(180deg,#d7dde3 0%,#c9ab86 38%,#e8e9ea 55%,#2e3550 72%,#1d2238 100%)}
.cover-photo{left:432px;top:128px;width:331px;height:258px}
.title{left:486px;top:411px;font-family:var(--display);font-size:30px;line-height:37px;letter-spacing:.2px}
.title .red{color:var(--red)}
.title .dark{color:var(--ink)}
.web-bar{left:462px;top:494px;width:301px;height:31px;background:var(--red);color:var(--white);font-size:12px;font-weight:500;display:flex;align-items:center;padding-left:24px}

/* inner spread */
.inner{left:217px;top:613px;width:764px;height:540px;background:var(--white)}
.fold{left:366px;top:0;width:30px;height:540px;background:linear-gradient(90deg,rgba(0,0,0,0) 0%,rgba(0,0,0,.08) 45%,rgba(0,0,0,.02) 55%,rgba(0,0,0,0) 100%)}
.side-col{left:0;top:0;width:186px;height:540px;background:var(--red)}
.inner-frame-top{left:22px;top:23px;width:260px;height:295px;border-left:4px solid var(--ink);border-top:4px solid var(--ink)}
.inner-frame-bottom{left:26px;top:309px;width:450px;height:4px;background:var(--ink)}
.inner-photo{left:34px;top:35px;width:476px;height:270px;background:linear-gradient(180deg,#f3e6c4 0%,#e2c48f 45%,#c9a066 70%,#b98e57 100%)}
.call-us{left:23px;top:335px;width:145px;color:var(--white)}
.call-us h2{font-size:12.5px;font-weight:700;line-height:16px;margin-bottom:7px}
.call-us p{font-size:8.3px;line-height:10.8px;text-align:justify}
.call-us .url{position:absolute;top:173px;font-size:11px;font-weight:500}
.help{left:203px;top:335px;width:157px}
.help h3{color:var(--red);font-size:11px;font-weight:700;line-height:14px;margin-bottom:7px}
.help ul{list-style:none}
.help li{position:relative;padding-left:9px;font-size:7.2px;line-height:9.2px;color:var(--text);text-align:justify;margin-bottom:8px}
.help li::before{content:"";position:absolute;left:0;top:2px;width:5px;height:5px;border-radius:50%;background:var(--red)}
.steps-head{left:537px;top:35px}
.steps-head h2{color:var(--red);font-size:18px;font-weight:500;line-height:22px}
.steps-head p{color:var(--ink);font-size:13px;font-weight:500;margin-top:2px}
.step{left:537px;width:210px;display:flex;gap:9px}
.step .icon{flex:0 0 44px;height:44px;border-radius:50%;border:2px solid var(--red);display:flex;align-items:center;justify-content:center}
.step .icon i{width:36px;height:36px;border-radius:50%;background:var(--red);display:flex;align-items:center;justify-content:center}
.step h4{color:var(--red);font-size:9.5px;font-weight:700;line-height:11px;margin-top:-4px}
.step p{font-size:7.2px;line-height:9.2px;color:var(--text);text-align:justify}
.step b{font-weight:500;color:var(--ink)}
.plans{left:405px;top:342px;width:335px;height:174px;background:linear-gradient(135deg,#dce9f4 0%,#b9d0e6 45%,#eef4f9 70%,#c6d9ec 100%)}
</style>
</head>
<body>
<div class="canvas">

  <section class="outer abs" aria-label="Outer spread">
    <div class="back-cover abs">
      <div class="back-brand abs brand">K&amp;B Restoration</div>
      <div class="contact-bar abs">
        <span><svg width="10" height="10" viewBox="0 0 10 10"><circle cx="5" cy="5" r="4.3" fill="none" stroke="#a6223b" stroke-width="1.2"/><path d="M3.4 2.8l1 .9-.5.7c.4.7.9 1.2 1.6 1.6l.7-.5.9 1-.6.7c-1.7-.3-3-1.6-3.4-3.4z" fill="#a6223b"/></svg>404.555.0173</span>
        <span><svg width="10" height="10" viewBox="0 0 10 10"><circle cx="5" cy="5" r="4.3" fill="none" stroke="#a6223b" stroke-width="1.2"/><circle cx="5" cy="5" r="2.3" fill="#a6223b"/></svg>K-B-Restoration.com</span>
      </div>
    </div>
    <div class="front-brand abs"><span class="name brand">K&amp;B Restoration</span></div>
    <div class="frame-top abs"></div>
    <div class="frame-bottom abs"></div>
    <div class="cover-photo photo abs" role="img" aria-label="Photo of a modern kitchen flooded with water"></div>
    <h1 class="title abs"><span class="red">INSURANCE CLAIM</span><br><span class="dark">SPECIALIST</span></h1>
    <div class="web-bar abs">K-B-Restoration.com</div>
  </section>

  <section class="inner abs" aria-label="Inner spread">
    <div class="side-col abs"></div>
    <div class="inner-frame-top abs"></div>
    <div class="inner-frame-bottom abs"></div>
    <div class="inner-photo abs" role="img" aria-label="Photo of a water-damaged home interior with debris and a piano"></div>

    <div class="call-us abs">
      <h2>WHEN WATER DAMAGE HAPPENS CALL US!</h2>
      <p>No one wants to deal with the headache that comes with water damage. Unexpected leaks, broken pipes or floods simply never occur at a convenient time. Should your home experience a water damage loss, big or small; call K&amp;B Restoration immediately to limit the damage to your property and expense of restoration.<br>Call us now at 404.555.0173!.</p>
      <div class="url">K-B-Restoration.com</div>
    </div>

    <div class="help abs">
      <h3>What we do to help you with a water damage</h3>
      <ul>
        <li>Would start with an inspection of the damage done, using special tools to find moisture</li>
        <li>Get to work right after the inspection. Extracting water, setting up dryers and dehumidifiers, and start drying the walls</li>
        <li>Continuous communication with you, answering any questions you have, &amp; working with you to solve situations.</li>
        <li>Monitoring the levels of humidity in the affected areas and removing equipment when finished.</li>
        <li>Finishing the job with sanitization and deodorization for your comfort and safety.</li>
      </ul>
    </div>

    <div class="fold abs"></div>

    <div class="steps-head abs">
      <h2>Water or Mold Damage?</h2>
      <p>What happens after the cleanup?</p>
    </div>

    <div class="step abs" style="top:85px">
      <div class="icon"><i><svg width="18" height="18" viewBox="0 0 18 18"><path d="M9 2c2.5 3.5 4.5 6 4.5 8.5a4.5 4.5 0 0 1-9 0C4.5 8 6.5 5.5 9 2z" fill="#fff"/></svg></i></div>
      <div><h4>ADJUSTER'S INSPECTION</h4><p><b>Feel Confident.</b> Be sure you received a fair &amp; accurate assessment &amp; repair of all damages with our team's use of industry leading Estimating Systems and On-Site Review.</p></div>
    </div>
    <div class="step abs" style="top:149px">
      <div class="icon"><i><svg width="18" height="18" viewBox="0 0 18 18"><path d="M4 2h10M4 16h10M5 2c0 4 4 5 4 7s-4 3-4 7M13 2c0 4-4 5-4 7s4 3 4 7" fill="none" stroke="#fff" stroke-width="1.6"/><path d="M6.5 14.5L9 11l2.5 3.5z" fill="#fff"/></svg></i></div>
      <div><h4>TIMELY SETTLEMENT</h4><p><b>Don't wait.</b> Minimize the hassle of long processing times from Estimate to Settlement when you team up with an Insurance Repair Specialist.</p></div>
    </div>
    <div class="step abs" style="top:212px">
      <div class="icon"><i><svg width="20" height="18" viewBox="0 0 20 18"><path d="M2 9L10 2l8 7" fill="none" stroke="#fff" stroke-width="2"/><path d="M4.5 8.5V16h4v-4h3v4h4V8.5L10 4z" fill="#fff"/></svg></i></div>
      <div><h4>UNDER ONE ROOF</h4><p><b>Don't Worry.</b> You won't need to arrange meetings with multiple contractors; we'll take care of everything from demo to final cleanup.</p></div>
    </div>
    <div class="step abs" style="top:275px">
      <div class="icon"><i><svg width="18" height="18" viewBox="0 0 18 18"><path d="M3 15L12 6M6 3l9 9M3 15l2 0 0-2" fill="none" stroke="#fff" stroke-width="2" stroke-linecap="round"/><circle cx="13" cy="5" r="2.4" fill="none" stroke="#fff" stroke-width="1.6"/></svg></i></div>
      <div><h4>SUPERIOR CRAFTSMANSHIP</h4><p><b>Don't settle for satisfactory.</b><br>Our team is committed to the highest standards of excellence every step of the way. Trust us when we say that we'll make you smile.</p></div>
    </div>

    <div class="plans abs" role="img" aria-label="Photo of rolled blue architectural plans"></div>
  </section>

</div>
</body>
</html>
```